Lone Mesa Haulworks Garage web site for repairs,Parts, Accessories and Off Road

Need a wed site design for our light duty truck repair shop, also need to be able to sell our products from this page as well. Has our logo as the headliner and brief description of what we do and our history. An example of what we would want it to work like can be seen at www.garvinsfuelworks.example . This is a good example of style and accesses ability to buy parts we have.

Target Market(s)

Light duty Diesel truck owners(Brell,Kastor,Vantorine)

Industry/Entity Type

Shop

Number of Pages Required

3 page

Font styles to use
Other font styles liked:
• The same font as our logo

Requirements
Must have
• A little about the shop and all of our services,availability to purchase our products, also a map of where we are located.
Nice to have
• I like the design of www.Garvinsfuelworks.example. Its easy to use and very descriptive of parts available

```html
<!DOCTYPE html>
<html lang="en">
<head>
<meta charset="utf-8">
<title>Lone Mesa Haulworks Garage</title>
<link rel="stylesheet" href="https://fonts.googleapis.com/css2?family=Montserrat:wght@400;600;700;800&family=Open+Sans:wght@400;600&display=swap">
<style>
:root{
  --navy:#1e2a38;
  --navy-deep:#141c26;
  --blue:#1d4f7c;
  --white:#ffffff;
  --ink:#1f2327;
  --grey-text:#5b6067;
  --rule:#cfd3d7;
  --footer-bg:#eceef0;
  --hero-a:#8fa4b8;
  --hero-b:#c9d2da;
  --hero-c:#5d6b78;
  --shop-a:#3d4650;
  --shop-b:#7c8791;
  --shop-c:#a9b1b8;
}
*{box-sizing:border-box;margin:0;padding:0}
html,body{width:753px;height:1200px;overflow:hidden;background:var(--white)}
body{font-family:"Open Sans",Arial,sans-serif;color:var(--ink);position:relative}
h1,h2,h3,.brand,.nav a,.btn{font-family:"Montserrat",Arial,sans-serif}

/* header */
.site-header{position:absolute;top:0;left:0;width:753px;height:40px;background:var(--navy);display:flex;align-items:center;padding:0 22px;z-index:3}
.brand{color:var(--white);font-weight:800;font-size:11px;letter-spacing:.5px;display:flex;align-items:center;gap:6px;width:170px}
.brand-mark{width:9px;height:9px;background:var(--white)}
.nav{display:flex;gap:22px;margin-left:28px}
.nav a{color:var(--white);font-size:7px;font-weight:600;text-decoration:none;letter-spacing:.5px}
.search{margin-left:auto;width:120px;height:14px;border:1px solid #8c97a3;background:#2a3746;display:flex;align-items:center;justify-content:flex-end;padding-right:3px}
.contact-btn{margin-left:10px;height:14px;padding:0 10px;border:1px solid var(--white);color:var(--white);font-size:6.5px;font-weight:600;display:flex;align-items:center;font-family:"Montserrat",Arial,sans-serif}

/* hero */
.hero{position:absolute;top:0;left:0;width:753px;height:325px;background:linear-gradient(180deg,var(--hero-b) 0%,var(--hero-a) 45%,var(--hero-c) 100%)}
.hero-title{position:absolute;left:150px;top:70px;color:var(--white);font-weight:800;font-size:37px;line-height:40px;letter-spacing:.5px;text-shadow:0 1px 3px rgba(0,0,0,.25)}
.about-btn{position:absolute;left:38px;top:262px;width:212px;height:48px;background:var(--navy-deep);color:var(--white);font-size:22px;font-weight:700;letter-spacing:1.5px;display:flex;align-items:center;justify-content:center}

/* intro */
.intro{position:absolute;top:325px;left:0;width:753px;height:190px;display:flex;padding:22px 38px 0}
.intro-col{flex:1}
.intro-col + .intro-col{border-left:1px solid var(--rule);padding-left:22px;margin-left:22px}
.intro h2{font-size:25px;font-weight:700;letter-spacing:.5px;margin-bottom:12px}
.intro p{font-size:8.2px;line-height:12px;color:var(--grey-text)}

/* services */
.services{position:absolute;top:515px;left:0;width:753px;height:350px;background:linear-gradient(100deg,var(--shop-a) 0%,var(--shop-b) 45%,var(--shop-c) 75%,var(--shop-b) 100%)}
.services h2{position:absolute;left:398px;top:75px;color:var(--white);font-size:50px;font-weight:800;line-height:52px;letter-spacing:1px}
.see-more{position:absolute;left:398px;top:182px;height:26px;padding:0 10px;background:var(--blue);color:var(--white);font-size:14px;font-weight:600;display:flex;align-items:center;gap:6px}

/* owner */
.owner{position:absolute;top:885px;left:0;width:753px;height:160px;padding:0 38px}
.owner h2{font-size:23px;font-weight:700;letter-spacing:.5px;margin-top:8px}
.owner-photo{position:absolute;left:88px;top:48px;width:90px;height:90px;border-radius:50%;background:linear-gradient(160deg,#d9dde0,#9aa6b1)}
.owner-info{position:absolute;left:250px;top:52px;width:465px}
.owner-info h3{font-size:13px;font-weight:600;margin-bottom:6px}
.owner-info p{font-size:7.6px;line-height:11px;color:var(--grey-text)}

/* footer */
.site-footer{position:absolute;top:1045px;left:0;width:753px;height:133px;background:var(--footer-bg);padding:10px 38px}
.footer-top{display:flex;align-items:center;gap:40px;font-size:6.5px;color:var(--grey-text);border-bottom:1px solid var(--rule);padding-bottom:8px}
.social{margin-left:auto;display:flex;gap:6px}
.social span{width:10px;height:10px;background:var(--navy)}
.footer-cols{display:flex;gap:30px;margin-top:10px}
.footer-col{width:110px}
.footer-col h3{font-size:7px;font-weight:700;margin-bottom:5px}
.footer-col ul{list-style:none;display:grid;grid-template-columns:1fr 1fr;gap:3px 8px}
.footer-col li{font-size:6px;color:var(--grey-text)}
.base-bar{position:absolute;bottom:0;left:0;width:753px;height:22px;background:var(--navy);display:flex;align-items:center;padding:0 38px;font-size:6px;color:#aeb7c1}
.base-bar nav{margin-left:auto;display:flex;gap:16px}
</style>
</head>
<body>

<section class="hero" role="img" aria-label="Photo of a row of white light duty pickup trucks parked outside the shop"></section>

<header class="site-header">
  <div class="brand"><span class="brand-mark"></span>LONE MESA HAULWORKS</div>
  <nav class="nav"><a>STOREFRONT</a><a>REPAIRS</a><a>ABOUT US</a><a>FAQ</a></nav>
  <div class="search"><svg width="8" height="8" viewBox="0 0 10 10"><circle cx="4" cy="4" r="3" fill="none" stroke="#fff" stroke-width="1.2"/><line x1="6.2" y1="6.2" x2="9" y2="9" stroke="#fff" stroke-width="1.2"/></svg></div>
  <div class="contact-btn">CONTACT</div>
</header>

<h1 class="hero-title">CERTIFIED COMPLETE<br>LIGHT DUTY TRUCK<br>DEALER</h1>
<div class="about-btn btn">ABOUT US</div>

<section class="intro">
  <div class="intro-col">
    <h2>SPECIALTIES</h2>
    <p>We are your dealer certified complete light duty diesel, gas, transmission, alignment and off road truck shop. We also carry a wide variety of truck accessories along with custom audio and fabrication in house. We have over 20 years experience and offer the best services and products for our customers that have grown with us.</p>
  </div>
  <div class="intro-col">
    <h2>HISTORY</h2>
    <p>Established in 2005. After working for a major dealership for over 10 years we opened our own shop that did not fit the usual dealer mold. Customers liked the personal attention and the honest technicians, and the latest technology in the equipment. We now offer the expertise of a dealer with the service and prices of a local garage you can trust.</p>
  </div>
</section>

<section class="services" role="img" aria-label="Photo of a technician working under the raised hood of a truck in the service bay">
  <h2>OUR<br>SERVICES</h2>
  <div class="see-more btn">see more <svg width="8" height="10" viewBox="0 0 8 10"><polyline points="2,1 6,5 2,9" fill="none" stroke="#fff" stroke-width="1.5"/></svg></div>
</section>

<section class="owner">
  <h2>BUSINESS OWNER</h2>
  <div class="owner-photo" role="img" aria-label="Portrait photo of the business owner"></div>
  <div class="owner-info">
    <h3>Dale R.</h3>
    <p>Graduated in 1996 from Prairie Ridge Technical College with a degree in diesel technology. After finishing school he went to work for a local dealer as a light line technician, became master certified in 1999 and senior master in 2002. Now in his twentieth year he is the owner and founder of Lone Mesa Haulworks Garage.</p>
  </div>
</section>

<footer class="site-footer">
  <div class="footer-top"><span>CLICK FOR</span><span>NEWSLETTER</span><div class="social"><span></span><span></span><span></span><span></span></div></div>
  <div class="footer-cols">
    <div class="footer-col"><h3>PRODUCT</h3><ul><li>Brakes</li><li>Wheels</li><li>Suspension</li><li>Lights</li><li>Exhaust</li><li>Audio</li></ul></div>
    <div class="footer-col"><h3>SERVICES</h3><ul><li>Diesel</li><li>Engines</li><li>Tires</li><li>Alignment</li><li>Off Road</li><li>Repairs</li></ul></div>
    <div class="footer-col"><h3>ABOUT US</h3><ul><li>About</li><li>History</li></ul></div>
    <div class="footer-col"><h3>CONTACT US</h3><ul><li>Location</li><li>Hours</li><li>Careers</li><li>Phone</li></ul></div>
  </div>
  <div class="base-bar"><span>© Lone Mesa Haulworks Garage. All rights reserved.</span><nav><span>Legal</span><span>Privacy Policy</span><span>Site Map</span><span>Terms</span></nav></div>
</footer>

</body>
</html>
```